Meridel Haulage - Website

A clean, not cluttered informative website for our business. We specialize in the transportation of radioactive materials across North America. The site is mostly for information about our company and will not be used to attract business but will be used to attract employee's mainly drivers. Driver's are very hard to find in our area. One of the pages needs to be a job's posting page with an apply now button. Either an application can be filled out there or a resume can be uploaded which ever functionality works better. I would like a website that I can easily edit, ability to change text and photos.

Number of Pages Required

5+ page

Colors

Designer to choose colors to be used in the design.

Requirements
Must have
• Home - About - Services - Jobs - Contact pages
• A way prospective employee's can apply or upload their resume to be emailed to me
• Very clean apperance
Should not have
• I don't want it to be busy

```html
<!DOCTYPE html>
<html lang="en">
<head>
<meta charset="utf-8">
<title>Meridel Haulage</title>
<link href="https://fonts.googleapis.com/css2?family=Roboto:wght@400;500;700&family=Open+Sans:wght@400;600&display=swap" rel="stylesheet">
<style>
:root{
  --blue:#10a8e8;
  --blue-dark:#0b8fc8;
  --ink:#222;
  --text:#8a8a8a;
  --line:#e4e4e4;
  --panel:#e6e6e6;
  --footer:#232323;
  --footer-text:#9a9a9a;
  --white:#fff;
}
*{box-sizing:border-box;margin:0;padding:0}
html,body{width:1200px;height:2946px;overflow:hidden}
body{position:relative;background:var(--white);font-family:"Roboto",Arial,sans-serif;color:var(--ink)}
.abs{position:absolute}
a{color:inherit;text-decoration:none}

/* header */
.topbar{left:420px;top:4px;font-size:10px;color:#777;display:flex;gap:40px;align-items:center;height:16px}
.topbar .item{display:flex;align-items:center;gap:6px}
.top-social{left:815px;top:7px;display:flex;gap:12px}
.top-social span{width:9px;height:9px;border-radius:50%;background:#7a7a7a;display:block}
.nav-band{left:360px;top:24px;width:840px;height:55px;background:var(--blue);clip-path:polygon(40px 0,100% 0,100% 100%,0 100%)}
.brand{left:222px;top:26px;font-family:"Roboto",sans-serif;font-weight:700;font-size:18px;color:#1d3a8a;letter-spacing:.5px}
.brand small{display:block;font-weight:400;font-size:9px;letter-spacing:4px;color:#1d3a8a;text-align:center}
.nav{left:458px;top:44px;display:flex;gap:26px;color:var(--white);font-size:15px;font-family:"Open Sans",sans-serif}

/* hero */
.hero{left:0;top:79px;width:1200px;height:498px;background:linear-gradient(170deg,#2f3a48 0%,#6b4a30 30%,#b86a2c 52%,#d08a3a 62%,#3a3230 82%,#1e1d22 100%)}
.hero-title{left:361px;top:259px;width:466px;height:41px;background:var(--blue);color:var(--white);font-family:"Open Sans",sans-serif;font-size:28px;text-align:center;line-height:41px}
.hero-sub{left:495px;top:306px;width:196px;height:40px;background:var(--blue);color:var(--white);font-family:"Open Sans",sans-serif;font-size:28px;text-align:center;line-height:40px;letter-spacing:1px}
.btn{height:30px;font-size:9px;font-weight:700;color:var(--white);text-align:center;line-height:30px;text-transform:uppercase}
.btn-solid{left:501px;top:359px;width:88px;background:var(--blue)}
.btn-ghost{left:599px;top:359px;width:90px;border:1px solid var(--white);line-height:28px}
.hero-arrow{top:315px;width:26px;height:32px;background:rgba(0,0,0,.35)}

/* features */
.feature-photo{width:190px;height:190px;border-radius:50%;border:6px solid #f0f0f0;top:486px}
.feature{width:220px;top:712px;text-align:center}
.feature h3{font-size:11px;font-weight:700;color:var(--blue);text-transform:uppercase;margin-bottom:8px}
.feature p{font-size:11px;line-height:16px;color:var(--text)}
.feature .more{display:block;margin-top:10px;font-size:8px;font-weight:700;color:var(--blue);text-transform:uppercase}
.pager{top:853px;left:530px;display:flex;align-items:center;gap:0}
.pager .rule{width:40px;height:1px;background:var(--line)}
.pager .dot{width:22px;height:22px;background:#ddd;margin:0 4px}

/* why choose */
.why-photo{left:6px;top:927px;width:593px;height:369px;background:linear-gradient(135deg,#3a3a3a,#bfbfbf 45%,#e8e8e8 55%,#1a1a1a)}
.why-panel{left:599px;top:927px;width:595px;height:369px;background:var(--blue)}
.why-title{left:640px;top:974px;color:var(--white);font-size:17px;font-weight:700}
.why-title::after{content:"";display:block;width:34px;height:2px;background:var(--white);margin-top:10px}
.why-icon{left:575px;width:44px;height:44px;border-radius:50%;background:var(--white);display:flex;align-items:center;justify-content:center}
.why-item{left:636px;width:420px;color:var(--white)}
.why-item h4{font-size:11px;font-weight:700;text-transform:uppercase;margin-bottom:6px}
.why-item p{font-size:11px;line-height:15px;opacity:.7}

/* who we are */
.sec-title{font-size:17px;font-weight:700;color:var(--ink);text-transform:uppercase}
.sec-title::after{content:"";display:block;width:44px;height:2px;background:var(--blue);margin-top:10px}
.accordion{left:244px;top:1390px;width:430px;height:320px;border:1px solid var(--line)}
.acc-head{left:256px;top:1408px;width:406px;font-size:11px;color:#555;display:flex;justify-content:space-between;text-transform:uppercase}
.about-photo{left:257px;top:1453px;width:187px;height:157px;background:linear-gradient(160deg,#2e5d8f,#d99436 55%,#6a4a2a)}
.about-copy{left:460px;top:1450px;width:200px}
.about-copy h4{font-size:13px;font-weight:700;margin-bottom:10px}
.about-copy p{font-size:11px;line-height:16px;color:var(--text);margin-bottom:10px}
.author{left:257px;top:1628px;font-size:11px;font-weight:700;color:#555}
.acc-row{left:256px;width:406px;font-size:11px;color:#555;display:flex;justify-content:space-between}

/* find jobs */
.jobs-head{left:731px;top:1328px;width:226px;height:55px;background:#111;color:var(--white);font-family:"Open Sans",sans-serif;font-size:27px;text-align:center;line-height:55px}
.jobs-form{left:731px;top:1383px;width:226px;height:253px;background:var(--panel)}
.field{position:absolute;background:var(--white);height:26px;font-size:8px;color:#aaa;padding:8px 0 0 6px;border:1px solid #d8d8d8}
.send{left:749px;top:1592px;width:68px;height:22px;background:var(--blue);color:var(--white);font-size:8px;font-weight:700;text-align:center;line-height:22px;text-transform:uppercase}

/* testimonial */
.avatar{left:565px;top:1777px;width:68px;height:68px;border-radius:50%;background:linear-gradient(135deg,#c9b8a2,#7a6a5a)}
.quote{left:400px;top:1866px;width:400px;text-align:center;font-size:10px;line-height:15px;color:var(--text)}
.quote-name{left:400px;top:1928px;width:400px;text-align:center;font-size:10px;font-weight:700;color:var(--blue);text-transform:uppercase}
.quote-role{left:400px;top:1944px;width:400px;text-align:center;font-size:9px;color:var(--text)}

/* news */
.news{width:226px;top:2178px}
.news-photo{width:226px;height:128px}
.news .meta{margin-top:22px;font-size:8px;color:#aaa}
.news h4{margin-top:8px;font-size:11px;font-weight:700;color:var(--blue)}
.news p{margin-top:6px;font-size:11px;line-height:16px;color:var(--text)}
.news .more{display:block;margin-top:10px;font-size:8px;font-weight:700;color:var(--blue);text-transform:uppercase}

/* clients */
.clients{left:270px;top:2585px;width:670px;display:flex;justify-content:space-between;align-items:center}
.clients span{font-family:"Roboto",sans-serif;font-size:14px;font-weight:500;color:#777}

/* footer */
.footer{left:0;top:2671px;width:1200px;height:275px;background:var(--footer)}
.f-title{top:2704px;font-size:11px;font-weight:700;color:var(--white);text-transform:uppercase}
.f-title::after{content:"";display:block;width:30px;height:2px;background:var(--blue);margin-top:10px}
.f-logo{left:244px;top:2727px;width:155px;height:56px;background:var(--white);color:#1d3a8a;font-weight:700;font-size:15px;display:flex;align-items:center;justify-content:center}
.f-about{left:244px;top:2786px;width:220px;font-size:11px;line-height:15px;color:var(--footer-text)}
.f-social{left:244px;top:2852px;display:flex;gap:6px}
.f-social span{width:18px;height:18px;border-radius:50%;border:1px solid #777;display:block}
.f-links{top:2750px;width:100px}
.f-links li{list-style:none;font-size:10px;color:var(--footer-text);padding:6px 0 6px;border-bottom:1px solid #333}
.f-contact{left:731px;width:230px;font-size:10px;line-height:14px;color:var(--footer-text);display:flex;gap:14px}
.to-top{left:1160px;top:2918px;width:24px;height:24px;border-radius:50%;background:#2f2f2f}
</style>
</head>
<body>

<!-- header -->
<div class="abs topbar">
  <span class="item"><svg width="8" height="8" viewBox="0 0 10 10"><path d="M2 1l2 2-1 1.5a6 6 0 0 0 2.5 2.5L7 6l2 2-1.5 1.5C4 9 1 6 .5 2.5z" fill="#777"/></svg>Phone: (+1) 0555 246 810</span>
  <span class="item"><svg width="9" height="7" viewBox="0 0 10 8"><rect x=".5" y=".5" width="9" height="7" fill="none" stroke="#777"/><path d="M.5.5 5 4.5 9.5.5" fill="none" stroke="#777"/></svg>Email: hello@meridelhaulage.co</span>
</div>
<div class="abs top-social"><span></span><span></span><span></span><span></span><span></span><span></span><span></span></div>
<div class="abs nav-band"></div>
<div class="abs brand">Meridel Haulage<small>TRANSPORT</small></div>
<nav class="abs nav"><a>Home</a><a>About Us</a><a>Service</a><a>Jobs</a><a>Contact Us</a></nav>

<!-- hero -->
<div class="abs hero" role="img" aria-label="Freight train of colourful shipping containers at sunset"></div>
<div class="abs hero-title">Meridel Haulage</div>
<div class="abs hero-sub">Logistics</div>
<a class="abs btn btn-solid">Our Service</a>
<a class="abs btn btn-ghost">Get a Quote</a>
<div class="abs hero-arrow" style="left:0"><svg width="26" height="32"><path d="M15 12l-4 4 4 4" stroke="#fff" fill="none" stroke-width="1.5"/></svg></div>
<div class="abs hero-arrow" style="left:1174px"><svg width="26" height="32"><path d="M11 12l4 4-4 4" stroke="#fff" fill="none" stroke-width="1.5"/></svg></div>

<!-- features -->
<div class="abs feature-photo" style="left:268px;background:linear-gradient(160deg,#f3d59a,#b43a2a 55%,#5a6470)" role="img" aria-label="Row of parked trucks"></div>
<div class="abs feature-photo" style="left:504px;background:linear-gradient(160deg,#c9d4dc,#d6c23a 55%,#5a5a52)" role="img" aria-label="Warehouse workers with a forklift"></div>
<div class="abs feature-photo" style="left:742px;background:linear-gradient(160deg,#3a4f8a,#e0562a 55%,#1a2540)" role="img" aria-label="Container ship at port at night"></div>

<div class="abs feature" style="left:253px"><h3>Paraging &amp; Storage</h3><p>Quisque ligulas ipsum, euismod atras vulputate iltricies etri elit. Class aptent taciti sociosqu ad litora torquent per conubia nostra, per inceptos himenaeos. Nulla...</p><a class="more">Read More &rarr;</a></div>
<div class="abs feature" style="left:489px"><h3>Contract Logistic</h3><p>Quisque ligulas ipsum, euismod atras vulputate iltricies etri elit. Class aptent taciti sociosqu ad litora torquent per conubia nostra, per inceptos himenaeos. Nulla...</p><a class="more">Read More &rarr;</a></div>
<div class="abs feature" style="left:727px"><h3>Safety and Reliability</h3><p>Quisque ligulas ipsum, euismod atras vulputate iltricies etri elit. Class aptent taciti sociosqu ad litora torquent per conubia nostra, per inceptos himenaeos. Nulla...</p><a class="more">Read More &rarr;</a></div>
<div class="abs pager"><span class="rule"></span><span class="dot"></span><span class="dot"></span><span class="rule"></span></div>

<!-- why choose us -->
<div class="abs why-photo" role="img" aria-label="White semi truck cab on a dark background"></div>
<div class="abs why-panel"></div>
<div class="abs why-title">WHY CHOOSE US</div>

<div class="abs why-icon" style="top:1044px"><svg width="20" height="20" viewBox="0 0 20 20"><circle cx="10" cy="10" r="8" fill="none" stroke="#10a8e8" stroke-width="2"/><path d="M10 5v5l3 2" stroke="#10a8e8" stroke-width="2" fill="none"/></svg></div>
<div class="abs why-item" style="top:1040px"><h4>Fast Transportion Service</h4><p>Qualified drivers move every load on schedule with careful route planning and full tracking.</p></div>
<div class="abs why-icon" style="top:1127px"><svg width="20" height="20" viewBox="0 0 20 20"><path d="M10 2l7 3v5c0 4-3 7-7 8-4-1-7-4-7-8V5z" fill="#10a8e8"/></svg></div>
<div class="abs why-item" style="top:1123px"><h4>Safety and Reliability</h4><p>Certified handling procedures and trained crews keep every sensitive shipment secure on the road.</p></div>
<div class="abs why-icon" style="top:1210px"><svg width="20" height="20" viewBox="0 0 20 20"><circle cx="10" cy="10" r="8" fill="none" stroke="#10a8e8" stroke-width="2"/><path d="M2 10h16M10 2c3 3 3 13 0 16M10 2c-3 3-3 13 0 16" stroke="#10a8e8" stroke-width="1.5" fill="none"/></svg></div>
<div class="abs why-item" style="top:1206px"><h4>Shipping Worldwide</h4><p>Our network reaches across the continent with dependable drivers and modern equipment.</p></div>

<!-- who we are -->
<h2 class="abs sec-title" style="left:244px;top:1343px">Who We Are</h2>
<div class="abs accordion"></div>
<div class="abs acc-head"><span>About Us</span><span>&minus;</span></div>
<div class="abs about-photo" role="img" aria-label="Truck on a highway at sunrise"></div>
<div class="abs about-copy">
  <h4>We transport all over the world</h4>
  <p>Lorem ipsum dolor sit amet, consectetur adipiscing elit, sed do eiusmod tempor incididunt ut labore et dolore magna aliqua. Ut enim ad minim veniam.</p>
  <p>It is anticipated the peak 15 minute frequency will remain in place for most of the day.</p>
</div>
<div class="abs author">Mr Tobias Renfrew</div>
<div class="abs acc-row" style="top:1661px"><span>our mission</span><span>+</span></div>
<div class="abs acc-row" style="top:1689px"><span>our vision</span><span>+</span></div>

<!-- find jobs -->
<div class="abs jobs-head">Find Jobs</div>
<div class="abs jobs-form"></div>
<div class="field" style="left:749px;top:1401px;width:190px">Your name</div>
<div class="field" style="left:749px;top:1432px;width:92px">Phone</div>
<div class="field" style="left:847px;top:1432px;width:92px">Email</div>
<div class="field" style="left:749px;top:1463px;width:190px">Cargo Type</div>
<div class="field" style="left:749px;top:1494px;width:190px">Destination</div>
<div class="field" style="left:749px;top:1525px;width:190px;height:55px">Your Messenger</div>
<a class="abs send">Send</a>

<!-- testimonial -->
<div class="abs avatar" role="img" aria-label="Portrait of the company founder"></div>
<p class="abs quote">We were looking for a logo with a touch of modernism. Our team grasped our needs and produced a superb result that shows clearly. Lorem ipsum dolor sit amet, consectetur end soure nemolo close-istras commisst</p>
<div class="abs quote-name">Mr. Tobias Renfrew</div>
<div class="abs quote-role">CEO &amp; Founder Meridel</div>

<!-- recent news -->
<h2 class="abs sec-title" style="left:244px;top:2121px">Recent News</h2>
<div class="abs news" style="left:244px">
  <div class="news-photo" style="background:linear-gradient(180deg,#8fb4d8,#d8dde2 55%,#c07a3a)" role="img" aria-label="Cargo plane being loaded on the tarmac"></div>
  <div class="meta">By Staff Writer / January 11th, 2016 / Transporter</div>
  <h4>Our sea will shipping the big</h4>
  <p>Quisque ligulas ipsum, euismod atras vulputate iltricies etri elit. Class aptent taciti sociosqu ad litora torquent per conubia nostra, per inceptos himenaeos. Nulla...</p>
  <a class="more">Read More &rarr;</a>
</div>
<div class="abs news" style="left:487px">
  <div class="news-photo" style="background:linear-gradient(180deg,#5aa8e0,#2a78b8 55%,#1a4a78)" role="img" aria-label="Container ship crossing the ocean"></div>
  <div class="meta">By Staff Writer / December 30th, 2015 / Blog</div>
  <h4>Shipping cargo across the ocean</h4>
  <p>Quisque ligulas ipsum, euismod atras vulputate iltricies etri elit. Class aptent taciti sociosqu ad litora torquent per conubia nostra, per inceptos himenaeos. Nulla...</p>
  <a class="more">Read More &rarr;</a>
</div>
<div class="abs news" style="left:731px">
  <div class="news-photo" style="background:linear-gradient(180deg,#f4f4f4,#e8c020 50%,#c0302a 75%,#eee)" role="img" aria-label="Colourful trucks with stacked parcels"></div>
  <div class="meta">By Staff Writer / December 30th, 2015 / Blog</div>
  <h4>Shipping car all international port</h4>
  <p>Quisque ligulas ipsum, euismod atras vulputate iltricies etri elit. Class aptent taciti sociosqu ad litora torquent per conubia nostra, per inceptos himenaeos. Nulla...</p>
  <a class="more">Read More &rarr;</a>
</div>

<!-- clients -->
<h2 class="abs sec-title" style="left:244px;top:2498px">Our Client</h2>
<div class="abs clients"><span>Northfield</span><span>Corvan</span><span>Halden Co</span><span>Brightmere</span><span>Ostwick</span><span>Tallow Pine</span></div>

<!-- footer -->
<footer class="abs footer"></footer>
<div class="abs f-title" style="left:244px">About Us</div>
<div class="abs f-logo">Meridel Haulage</div>
<p class="abs f-about">ut labore et dolore magna aliqua. Ut enim ad minim veniam, quis nostrud exercitation ullamco laboris nisi ut aliquip ex ea commodo consequat.</p>
<div class="abs f-social"><span></span><span></span><span></span><span></span><span></span><span></span><span></span></div>

<div class="abs f-title" style="left:487px">Quick Link</div>
<ul class="abs f-links" style="left:487px"><li>About us</li><li>Location</li><li>Site maps</li><li>Get a quote</li><li>Information</li></ul>
<ul class="abs f-links" style="left:609px"><li>Ocean freight</li><li>Storage</li><li>Security</li><li>Air freight</li><li>Warehousing</li></ul>

<div class="abs f-title" style="left:731px">Contact Us</div>
<div class="abs f-contact" style="top:2750px"><svg width="10" height="13" viewBox="0 0 10 13"><path d="M5 0a5 5 0 0 1 5 5c0 3-5 8-5 8S0 8 0 5a5 5 0 0 1 5-5z" fill="#777"/><circle cx="5" cy="5" r="2" fill="#232323"/></svg><span>Suite 501 - 169 Larch Ridge Road<br>Eastgate District - Harrow City</span></div>
<div class="abs f-contact" style="top:2795px"><svg width="10" height="10" viewBox="0 0 10 10"><path d="M2 1l2 2-1 1.5a6 6 0 0 0 2.5 2.5L7 6l2 2-1.5 1.5C4 9 1 6 .5 2.5z" fill="#777"/></svg><span>(+1) 0555 246 810<br>(+1) 0555 864 213</span></div>
<div class="abs f-contact" style="top:2847px"><svg width="10" height="8" viewBox="0 0 10 8"><rect x=".5" y=".5" width="9" height="7" fill="none" stroke="#777"/><path d="M.5.5 5 4.5 9.5.5" fill="none" stroke="#777"/></svg><span>http://meridelhaulage.co<br>hello@meridelhaulage.co</span></div>
<div class="abs to-top"><svg width="24" height="24"><path d="M8 14l4-4 4 4" stroke="#888" fill="none"/></svg></div>

</body>
</html>
```